BriskwayLane.com needs updated website design.

BriskwayLane.com offers individuals a quick, hassle-free way of selling their car, rv, or boat in the Sun City Center, FL area. We will come to the customer's place of choosing in order to give them an in-person offer for their car, rv, or boat. Looking for a website design that will allow users to input their vehicle details as well as their contact info in order to schedule a time and place for our staff to come make them an offer. Currently have an active site that can be referenced.

Target Market(s)

Older people who no longer need their cars.

Industry/Entity Type

Automotive

Coding

Coded - Design and coding required

Number of Pages Required

3 page

Font styles to use
Sans Serif

Colors
a1cd3a
33b8a4

Requirements
Must have
• Trustworthy theme, Emphasis on capturing contact info (contact form visible at all times). Standard privacy policy. Wordpress theme

```html
<!DOCTYPE html>
<html lang="en">
<head>
<meta charset="utf-8">
<title>BriskwayLane.com</title>
<link href="https://fonts.googleapis.com/css2?family=Roboto:wght@400;500;700&display=swap" rel="stylesheet">
<style>
:root{
  --green:#a1cd3a;
  --teal:#33b8a4;
  --navy:#1b3a66;
  --ink:#111;
  --text:#555;
  --grey-line:#e2e2e2;
  --footer:#161616;
  --white:#fff;
}
*{margin:0;padding:0;box-sizing:border-box}
html,body{width:1200px;height:2824px;overflow:hidden}
body{position:relative;font-family:'Roboto',sans-serif;background:var(--white);color:var(--ink)}
a{color:inherit;text-decoration:none}

/* header */
.site-header{position:absolute;left:0;top:0;width:1200px;height:80px;border-top:4px solid var(--navy);background:var(--white)}
.brand{position:absolute;left:88px;top:18px;display:flex;align-items:center;gap:14px}
.brand-name{font-weight:700;font-size:23px;color:#3a3a3a;line-height:1}
.brand-dot{width:40px;height:40px;border-radius:50%;background:var(--teal)}
.main-nav{position:absolute;top:30px;font-size:15px;letter-spacing:.4px;color:#222}
.main-nav a{position:absolute;white-space:nowrap;transform:translateX(-50%)}
.main-nav a.active{color:var(--teal)}

/* hero */
.hero{position:absolute;left:0;top:80px;width:1200px;height:603px;
  background:linear-gradient(100deg,#2c3a44 0%,#3f5660 30%,#6b7f80 48%,#b6b59c 70%,#d9d6b2 100%)}
.hero-title{position:absolute;left:88px;top:284px;font-size:49px;font-weight:700;color:var(--white);line-height:1}
.hero-sub{position:absolute;left:88px;top:344px;font-size:35px;font-weight:700;color:var(--white);line-height:1}
.btn{position:absolute;display:flex;align-items:center;justify-content:center;border-radius:25px;font-weight:500;font-size:16px;color:var(--white)}
.btn-green{background:var(--green)}
.btn-teal{background:var(--teal)}
.btn-white{background:var(--white);color:var(--teal)}

.quote-panel{position:absolute;left:660px;top:198px;width:450px;height:361px;background:#7f7f76}
.tab{position:absolute;top:6px;width:121px;height:40px;display:flex;align-items:center;justify-content:center;font-weight:500;font-size:16px;color:var(--white);background:var(--teal)}
.tab.active{background:var(--white);color:var(--teal)}
.quote-form{position:absolute;left:5px;top:52px;width:440px;height:309px;background:var(--teal)}
.field{position:absolute;width:210px;height:45px;background:var(--white);font-size:15px;color:#777;padding:14px 15px;display:flex;justify-content:space-between}
.field svg{width:10px;height:10px;margin-top:3px}
.submit{position:absolute;left:6px;top:259px;width:428px;height:44px;background:var(--green);color:var(--white);font-weight:500;font-size:16px;display:flex;align-items:center;justify-content:center}

/* features */
.feature{position:absolute;top:771px;width:260px;text-align:center;transform:translateX(-50%)}
.feature-icon{width:103px;height:103px;margin:0 auto;border:2px solid var(--green);border-radius:50%;display:flex;align-items:center;justify-content:center}
.feature h3{font-size:18px;font-weight:500;margin-top:17px;color:#111}
.feature p{font-size:14px;color:#444;margin-top:10px}

/* about */
.frame-green{position:absolute;background:var(--green)}
.photo{position:absolute}
.section-title{position:absolute;font-size:37px;font-weight:700;color:var(--ink)}
.about-text{position:absolute;left:639px;top:1158px;width:482px;font-size:16.5px;line-height:33px;color:var(--text)}

/* offer band */
.offer-band{position:absolute;left:0;top:1539px;width:1200px;height:319px;background:var(--teal);text-align:center;color:var(--white)}
.offer-band h2{position:absolute;left:0;width:100%;top:72px;font-size:35px;font-weight:700}
.offer-band p{position:absolute;left:0;width:100%;top:120px;font-size:36px;font-weight:700}

/* faq */
.faq-item{position:absolute;left:90px;width:479px;border-bottom:1px solid var(--grey-line)}
.faq-item h4{font-size:16px;font-weight:500;color:#111}
.faq-item p{font-size:16px;color:#666;margin-top:8px;line-height:19px;max-width:385px}

/* footer */
.site-footer{position:absolute;left:0;top:2460px;width:1200px;height:364px;background:var(--footer);color:var(--white)}
.foot-brand{position:absolute;left:90px;top:60px;display:flex;align-items:center;gap:14px}
.foot-brand .brand-name{color:#4a4a4a;font-size:26px}
.foot-brand .brand-dot{width:56px;height:56px}
.foot-col{position:absolute;top:66px}
.foot-col h5{font-size:18px;font-weight:500;margin-bottom:18px}
.foot-col li{list-style:none;font-size:13.5px;height:27px;display:flex;align-items:center;gap:12px;color:var(--white)}
.soc{width:11px;height:11px;background:var(--white);border-radius:2px}
.copyright{position:absolute;left:90px;top:305px;font-size:13.5px;line-height:23px}
</style>
</head>
<body>

<header class="site-header">
  <div class="brand">
    <div class="brand-name">BriskwayLane.com</div>
    <div class="brand-dot"></div>
  </div>
  <nav class="main-nav">
    <a class="active" style="left:534px">Home</a>
    <a style="left:637px">About Us</a>
    <a style="left:751px">Services</a>
    <a style="left:864px">Our Work</a>
    <a style="left:962px">Blog</a>
    <a style="left:1069px">Contact Us</a>
  </nav>
</header>

<section class="hero" role="img" aria-label="Photo of a dark sedan parked by the sea under a pale sky"></section>
<h1 class="hero-title">BriskwayLane.com</h1>
<p class="hero-sub">I’ll Buy You Car Boat RV Today</p>
<a class="btn btn-green" style="left:90px;top:427px;width:163px;height:45px">READ MORE</a>

<div class="quote-panel">
  <div class="tab active" style="left:5px">CAR</div>
  <div class="tab" style="left:133px">RV</div>
  <div class="tab" style="left:261px">BOAT</div>
  <form class="quote-form">
    <div class="field" style="left:6px;top:5px">Vehicle<svg viewBox="0 0 10 10"><path d="M1 3l4 4 4-4" fill="none" stroke="#888" stroke-width="1.3"/></svg></div>
    <div class="field" style="left:223px;top:5px">Make<svg viewBox="0 0 10 10"><path d="M1 3l4 4 4-4" fill="none" stroke="#888" stroke-width="1.3"/></svg></div>
    <div class="field" style="left:6px;top:56px">Model<svg viewBox="0 0 10 10"><path d="M1 3l4 4 4-4" fill="none" stroke="#888" stroke-width="1.3"/></svg></div>
    <div class="field" style="left:223px;top:56px">Year<svg viewBox="0 0 10 10"><path d="M1 3l4 4 4-4" fill="none" stroke="#888" stroke-width="1.3"/></svg></div>
    <div class="field" style="left:6px;top:106px">Date<svg viewBox="0 0 10 10"><path d="M1 3l4 4 4-4" fill="none" stroke="#888" stroke-width="1.3"/></svg></div>
    <div class="field" style="left:223px;top:106px">Time<svg viewBox="0 0 10 10"><path d="M1 3l4 4 4-4" fill="none" stroke="#888" stroke-width="1.3"/></svg></div>
    <div class="field" style="left:6px;top:157px">Name</div>
    <div class="field" style="left:223px;top:157px">Phone No</div>
    <div class="field" style="left:6px;top:208px">Email Address</div>
    <div class="field" style="left:223px;top:208px">Address</div>
    <div class="submit">SUBMIT</div>
  </form>
</div>

<section>
  <div class="feature" style="left:170px">
    <div class="feature-icon"><svg width="50" height="50" viewBox="0 0 50 50" fill="none" stroke="#a1cd3a" stroke-width="2"><circle cx="29" cy="25" r="15"/><path d="M29 16v9l6 4M4 20h9M2 26h11M6 32h8"/></svg></div>
    <h3>FAST</h3><p>I’ll Be at Your Door Today</p>
  </div>
  <div class="feature" style="left:455px">
    <div class="feature-icon"><svg width="50" height="50" viewBox="0 0 50 50" fill="none" stroke="#a1cd3a" stroke-width="2"><circle cx="25" cy="12" r="7"/><circle cx="12" cy="30" r="4"/><circle cx="38" cy="30" r="4"/><path d="M5 45c0-6 3-9 7-9s7 3 7 9M31 45c0-6 3-9 7-9s7 3 7 9M19 38h12"/></svg></div>
    <h3>FAIR</h3><p>Get Fair Price for Your Vehicle</p>
  </div>
  <div class="feature" style="left:740px">
    <div class="feature-icon"><svg width="50" height="50" viewBox="0 0 50 50" fill="none" stroke="#a1cd3a" stroke-width="2"><circle cx="25" cy="25" r="17"/><path d="M17 25l6 6 11-12"/></svg></div>
    <h3>FRIENDLY</h3><p>Trusted for Over 25 Years</p>
  </div>
  <div class="feature" style="left:1025px">
    <div class="feature-icon"><svg width="50" height="50" viewBox="0 0 50 50" fill="none" stroke="#a1cd3a" stroke-width="2"><rect x="10" y="24" width="7" height="18"/><path d="M17 26l7-9v-5h4v11h10l-3 19H17M25 3v5M15 8l3 3M35 8l-3 3"/></svg></div>
    <h3>HASSLE FREE</h3><p>I Handle All the Paperwork</p>
  </div>
</section>

<section>
  <div class="frame-green" style="left:80px;top:1031px;width:499px;height:429px"></div>
  <div class="photo" style="left:90px;top:1023px;width:497px;height:428px;background:linear-gradient(135deg,#dcdcd0,#b9bfa8 45%,#3a3a36 75%,#22221f)" role="img" aria-label="Photo of a person in a suit holding out a fan of banknotes"></div>
  <h2 class="section-title" style="left:639px;top:1097px">ABOUT US</h2>
  <p class="about-text">We offer the most convenient way of selling your vehicle. We will come to you at a place of your choosing, i.e. home, office, or any other public place.&nbsp; We will give you an in person cash offer on the spot.</p>
  <a class="btn btn-teal" style="left:639px;top:1318px;width:167px;height:50px">READ MORE</a>
</section>

<section class="offer-band">
  <h2>GET YOUR FREE IN PERSON CASH OFFER TODAY</h2>
  <p>“Don’t Sell Til You Give Me A Yell”</p>
  <a class="btn btn-white" style="left:517px;top:191px;width:166px;height:50px">CONTACT US</a>
</section>

<section>
  <h2 class="section-title" style="left:88px;top:1948px">FAQ</h2>
  <div class="faq-item" style="top:2023px;height:61px">
    <h4>Got an old clunker? I’ll But It!</h4><p>Turn it into cash today!</p>
  </div>
  <div class="faq-item" style="top:2101px;height:85px">
    <h4>Got a nice car you just don’t need? I’ll Buy It!</h4><p>Stop wasting money on insurance, registration and maintenance costs!</p>
  </div>
  <div class="faq-item" style="top:2200px;height:65px">
    <h4>Got a car that needs repairs? I’ll Buy It!</h4><p>No matter what the issue is I’ll come take it away today!</p>
  </div>
  <a class="btn btn-teal" style="left:90px;top:2311px;width:167px;height:50px">CONTACT US</a>
  <div class="frame-green" style="left:622px;top:1954px;width:497px;height:429px"></div>
  <div class="photo" style="left:613px;top:1945px;width:497px;height:429px;background:linear-gradient(180deg,#dfe6e2 0%,#9fb08a 22%,#5f7a3e 45%,#6d7770 70%,#4a4f4c 100%)" role="img" aria-label="Photo of a white SUV driving on a country road past green hills"></div>
</section>

<footer class="site-footer">
  <div class="foot-brand">
    <div class="brand-name">BriskwayLane.com</div>
    <div class="brand-dot"></div>
  </div>
  <div class="foot-col" style="left:541px">
    <h5>LINKS</h5>
    <ul><li>Home</li><li>About Us</li><li>Services</li><li>Our Work</li><li>Blog</li><li>Contact Us</li></ul>
  </div>
  <div class="foot-col" style="left:743px">
    <h5>CONTACT US</h5>
    <ul><li>Phone Number</li><li>555-014-2290</li><li></li><li>Email Address</li><li>info@briskwaylane.com</li></ul>
  </div>
  <div class="foot-col" style="left:1012px">
    <h5>FOLLOW US</h5>
    <ul><li><span class="soc"></span>Pinwheel</li><li><span class="soc"></span>Snapfold</li><li><span class="soc"></span>Chirper</li><li><span class="soc"></span>Streamly</li></ul>
  </div>
  <p class="copyright">© 2020 The Company name. All rights Reserved |<br>Privacy and Terms of use</p>
</footer>

</body>
</html>
```